Web Design for historic veg friendly, organic restaurant

We need a new web site. The Brookmere Cafe is a 40 year old restaurant in Chicago. We've been one of the premier, casual vegetarian restaurants since we opened. 5 years ago, Brookmere Cafe was purchased from the original owners by a local, certified organic farmer. We are nearly 100% from scratch kitchen, 100% certified organic produce, we are governed by a strict sustainable plan and we are very active politically. But you wouldn't know it form our website! We have a desire to build a simple website around some basic principles:
1. We need our current logo prominently displayed (logo attached)
2. We need a "click to call" easily accessible
3. We have an online order link that needs to be easily accessible
4. We need our hours, location, and directions easy to see
4. We need a separate events page (we have a live music and events venue that runs shows 5-7 nights per week.)
5. We would like to have a separate page for pictures, particularly old pictures. It would be fun to have a function for people to post their own shots, but that might make this too complicated. If it were possible, we would of course need to retain the ability to curate posted pictures.
6. This needs to be easily edited by us, so in a platform such as word press or similar
7. We will need this mobile enhanced

Target Market(s)

Neighborhood residents - zip code is 60626

Industry/Entity Type

Restaurant

Coding

Coded - Design and coding required

Number of Pages Required

4 page

Font styles to use
Sans Serif

Requirements
Must have
• Logo, click to call, events page that we can manage, contact us, about us page, menu (we have the online menu through a third party plugin), a page for our market and some nice pictures on our splash page,
• Must be mobile ready and on a platform such as Word Press or some other platform where we can edit on our own
Nice to have
• Page for past employees and historical pictures, be nice to have food pictures or something similar on a scroll, would love to have an ability for others to post pictures that we would "approve"
Should not have
• We don't need anything that spins, moves, flames or other features that detract from gathering information

```html
<!DOCTYPE html>
<html lang="en">
<head>
<meta charset="utf-8">
<title>Brookmere Cafe</title>
<link href="https://fonts.googleapis.com/css2?family=Cinzel:wght@400;700&family=Great+Vibes&family=Open+Sans:wght@400;600;700&display=swap" rel="stylesheet">
<style>
:root{
  --yellow:#f6d80c;
  --ink:#151316;
  --night:#1f1b21;
  --plum:#2e2632;
  --red:#d9302c;
  --paper:#ffffff;
  --mist:#ececec;
  --grey:#9a9a9a;
  --line:#f2b8b5;
}
*{box-sizing:border-box;margin:0;padding:0}
html,body{width:1200px;height:4500px;overflow:hidden}
body{position:relative;background:var(--mist);font-family:"Open Sans",Arial,sans-serif;color:var(--ink)}
.abs{position:absolute}
.photo{position:absolute}
.script{font-family:"Great Vibes",cursive;color:var(--red)}
.serif{font-family:"Cinzel",Georgia,serif}
.btn{position:absolute;display:flex;align-items:center;justify-content:center;font-size:15px;font-weight:600;border-radius:4px}
.btn-dark{background:var(--ink);color:var(--paper);border:2px solid var(--yellow)}
.btn-black{background:var(--ink);color:var(--paper)}

/* header */
.topbar{position:absolute;left:0;top:0;width:1200px;height:64px;background:rgba(20,18,22,.85);z-index:3}
.topbar .phone{position:absolute;right:130px;top:20px;color:var(--paper);font-size:17px;display:flex;gap:8px;align-items:center}
.topbar .social{position:absolute;right:40px;top:24px;display:flex;gap:10px}
.topbar .social span{width:16px;height:16px;border-radius:50%;background:var(--paper);opacity:.8}
.nav{position:absolute;left:470px;top:64px;width:730px;height:46px;background:var(--yellow);z-index:3;display:flex;justify-content:flex-end;gap:38px;padding-right:40px;align-items:center;font-size:14px;font-weight:700}
.nav a{color:var(--ink);text-decoration:none}
.nav a.active{color:var(--paper)}
.brand{position:absolute;left:40px;top:18px;z-index:4;display:flex;align-items:center;gap:12px;background:var(--yellow);padding:16px 22px;border-radius:8px}
.brand .dot{width:26px;height:26px;border-radius:50%;background:var(--red)}
.brand .name{font-weight:700;font-size:28px;color:var(--red)}

/* hero */
.hero{position:absolute;left:0;top:0;width:1200px;height:730px}
.hero .plate{position:absolute;left:230px;top:370px;width:700px;height:280px;border-radius:50% 50% 40% 40%;background:radial-gradient(ellipse,#d9a45c 0%,#a8652f 55%,rgba(90,50,40,0) 75%)}
.hero .table{position:absolute;left:0;top:560px;width:1200px;height:170px;background:linear-gradient(#6b3a24,#3a2016)}
.hero .disc{position:absolute;top:150px;width:100%;text-align:center;color:var(--paper);font-size:58px}
.hero .title{position:absolute;top:215px;width:100%;text-align:center;color:var(--paper);font-size:76px;letter-spacing:4px}
.hero .dots{position:absolute;top:682px;left:568px;display:flex;gap:12px}
.hero .dots span{width:14px;height:14px;border-radius:50%;border:2px solid var(--paper)}
.hero .dots span.on{background:var(--red);border-color:var(--red)}

/* welcome */
.welcome-card{position:absolute;left:70px;top:830px;width:320px;height:400px;background:var(--paper);border:6px solid #dedede;text-align:center;padding-top:40px}
.welcome-card .script{font-size:34px}
.welcome-card h2{font-size:34px;font-weight:400;margin:6px 0 22px}
.welcome-card p{font-size:13px;line-height:1.7;color:#555;padding:0 34px}

/* menu */
.menu{position:absolute;left:0;top:1320px;width:1200px;height:840px;background:radial-gradient(ellipse at 50% 50%,#2e2a2c,#0f0d10);clip-path:polygon(0 6%,100% 0,100% 94%,0 100%)}
.menu .disc{position:absolute;top:120px;width:100%;text-align:center;color:var(--paper);font-size:30px}
.menu h2{position:absolute;top:158px;width:100%;text-align:center;color:var(--paper);font-weight:400;font-size:42px}
.dish{position:absolute;width:490px;height:72px}
.dish .thumb{position:absolute;left:0;top:4px;width:90px;height:64px;border-radius:4px;background:radial-gradient(circle,#c9863e,#5b3420)}
.dish .n{position:absolute;left:104px;top:6px;color:var(--yellow);font-size:14px;font-weight:700}
.dish .d{position:absolute;left:104px;top:32px;color:#bdbdbd;font-size:12px}
.dish .p{position:absolute;right:0;top:14px;color:var(--paper);font-size:20px;font-weight:600}

/* events */
.events-head .script{position:absolute;top:2160px;width:100%;text-align:center;font-size:34px}
.events-head h2{position:absolute;top:2196px;width:100%;text-align:center;font-weight:400;font-size:42px}
.ev-card{position:absolute;background:var(--paper);text-align:center}
.ev-card .script{font-size:24px}
.ev-card h3{font-family:"Cinzel",Georgia,serif;font-weight:400;font-size:26px;margin-top:4px}
.ev-card .more{font-family:"Great Vibes",cursive;color:var(--red);font-size:22px;text-decoration:underline;display:block;margin-top:6px}
.ev-card p{font-size:12px;line-height:1.7;color:#555;padding:0 26px;margin-top:16px}

/* order band */
.order{position:absolute;left:0;top:2820px;width:1200px;height:250px;background:linear-gradient(90deg,#141216,#2a2428 50%,#141216);clip-path:polygon(0 10%,100% 0,100% 90%,0 100%)}
.order .label{position:absolute;color:var(--paper);font-size:20px;font-weight:600}
.order .sub{position:absolute;color:var(--yellow);font-size:14px}
.order-plate{position:absolute;left:490px;top:2840px;width:220px;height:220px;border-radius:50%;background:radial-gradient(circle,#8fb35a 0%,#c25c3a 45%,#f2eee8 70%,#d8d2cc 100%);box-shadow:0 8px 20px rgba(0,0,0,.4)}

/* gallery */
.tabs{position:absolute;left:120px;top:3150px;width:960px;height:44px;border-top:1px solid var(--line);border-bottom:1px solid var(--line);display:flex;justify-content:center;gap:44px;align-items:center;font-size:14px;color:var(--line)}
.tabs .on{color:var(--ink);font-weight:700}

/* footer */
.footer{position:absolute;left:0;top:4030px;width:1200px;height:400px;background:linear-gradient(var(--plum),#3a2f3c)}
.footer h4{position:absolute;top:40px;font-family:"Great Vibes",cursive;color:var(--yellow);font-size:28px;font-weight:400}
.footer ul{position:absolute;left:80px;top:92px;list-style:none;color:#d8d2da;font-size:14px;line-height:26px}
.footer ul li::before{content:"";display:inline-block;width:6px;height:6px;border-radius:50%;background:var(--yellow);margin-right:10px;vertical-align:middle}
.footer .row{position:absolute;left:320px;display:flex;gap:14px;color:#d8d2da;font-size:14px;line-height:22px}
.footer .row b{color:var(--yellow)}
.foot-brand{position:absolute;left:880px;top:60px;display:flex;align-items:center;gap:12px;background:var(--yellow);padding:14px 20px;border-radius:8px}
.foot-brand .dot{width:24px;height:24px;border-radius:50%;background:var(--red)}
.foot-brand .name{font-weight:700;font-size:26px;color:var(--red)}
.bottombar{position:absolute;left:0;top:4430px;width:1200px;height:70px;background:var(--yellow);display:flex;align-items:center;justify-content:flex-end;padding-right:80px;font-size:14px}
</style>
</head>
<body>

<header>
  <div class="topbar">
    <div class="phone">
      <svg width="18" height="18" viewBox="0 0 24 24"><path fill="#fff" d="M6.6 10.8a15 15 0 0 0 6.6 6.6l2.2-2.2a1 1 0 0 1 1-.25 11 11 0 0 0 3.6.6 1 1 0 0 1 1 1V20a1 1 0 0 1-1 1A17 17 0 0 1 3 4a1 1 0 0 1 1-1h3.5a1 1 0 0 1 1 1c0 1.25.2 2.45.6 3.6a1 1 0 0 1-.25 1z"/></svg>
      (312) 555-0148
    </div>
    <div class="social"><span></span><span></span><span></span></div>
  </div>
  <div class="brand"><span class="dot"></span><span class="name">Brookmere Cafe</span></div>
  <nav class="nav">
    <a class="active" href="#">HOME</a><a href="#">ABOUT</a><a href="#">MENU</a><a href="#">EVENTS</a><a href="#">GALLERY</a><a href="#">CONTACT</a>
  </nav>
</header>

<section class="hero">
  <div class="photo" role="img" aria-label="Grilled wraps with fresh vegetables on a wooden table" style="inset:0;background:radial-gradient(ellipse at 50% 65%,#a86a44 0%,#6a3c3e 40%,#2d2030 100%)"></div>
  <div class="table" role="img" aria-label="Wooden table surface"></div>
  <div class="plate" role="img" aria-label="Wrapped sandwiches with salad"></div>
  <div class="disc script" style="color:#fff">Discover</div>
  <div class="title serif">ROYAL PLATE</div>
  <div class="dots"><span class="on"></span><span></span><span></span></div>
</section>

<section class="welcome">
  <div class="welcome-card">
    <div class="script">Welcome</div>
    <h2 class="serif">Brookmere Cafe</h2>
    <p>A friendly neighborhood table serving fresh, scratch made plates with seasonal organic produce, good coffee and warm service every day.</p>
    <div class="btn btn-black" style="left:100px;top:300px;width:108px;height:40px;font-size:13px">Learn More</div>
  </div>
  <div class="photo" role="img" aria-label="Plate of pasta with herbs" style="left:450px;top:780px;width:370px;height:470px;background:radial-gradient(circle at 50% 55%,#6b6a62 0%,#3a3c3e 45%,#dcdcdc 46%,#f1f1f1 100%)"></div>
  <div class="photo" role="img" aria-label="Bowl of roasted vegetables with tomatoes" style="left:820px;top:830px;width:320px;height:470px;background:radial-gradient(circle at 50% 50%,#b6452c 0%,#7c2a1e 35%,#e8e4de 37%,#1c1a1c 60%)"></div>
</section>

<section class="menu">
  <div class="disc script" style="color:#fff">Discover</div>
  <h2 class="serif">OUR MENU</h2>
  <div class="dish" style="left:70px;top:240px"><div class="thumb" role="img" aria-label="Loaded fries"></div><div class="n">QUESO LOADED FRIES</div><div class="d">Crispy fries | queso | chipotle ranch</div><div class="p">$10.99</div></div>
  <div class="dish" style="left:70px;top:330px"><div class="thumb" role="img" aria-label="Loaded fries"></div><div class="n">QUESO LOADED FRIES</div><div class="d">Crispy fries | queso | chipotle ranch</div><div class="p">$10.99</div></div>
  <div class="dish" style="left:70px;top:420px"><div class="thumb" role="img" aria-label="Loaded fries"></div><div class="n">QUESO LOADED FRIES</div><div class="d">Crispy fries | queso | chipotle ranch</div><div class="p">$10.99</div></div>
  <div class="dish" style="left:70px;top:510px"><div class="thumb" role="img" aria-label="Loaded fries"></div><div class="n">QUESO LOADED FRIES</div><div class="d">Crispy fries | queso | chipotle ranch</div><div class="p">$10.99</div></div>
  <div class="dish" style="left:640px;top:240px"><div class="thumb" role="img" aria-label="Loaded fries"></div><div class="n">QUESO LOADED FRIES</div><div class="d">Crispy fries | queso | chipotle ranch</div><div class="p">$10.99</div></div>
  <div class="dish" style="left:640px;top:330px"><div class="thumb" role="img" aria-label="Loaded fries"></div><div class="n">QUESO LOADED FRIES</div><div class="d">Crispy fries | queso | chipotle ranch</div><div class="p">$10.99</div></div>
  <div class="dish" style="left:640px;top:420px"><div class="thumb" role="img" aria-label="Loaded fries"></div><div class="n">QUESO LOADED FRIES</div><div class="d">Crispy fries | queso | chipotle ranch</div><div class="p">$10.99</div></div>
  <div class="dish" style="left:640px;top:510px"><div class="thumb" role="img" aria-label="Loaded fries"></div><div class="n">QUESO LOADED FRIES</div><div class="d">Crispy fries | queso | chipotle ranch</div><div class="p">$10.99</div></div>
  <div class="btn btn-dark" style="left:505px;top:636px;width:190px;height:44px">Explore Full Menu</div>
</section>

<section class="events">
  <div class="events-head"><div class="script">To Day</div><h2 class="serif">EVENTS</h2></div>
  <div class="ev-card" style="left:80px;top:2250px;width:260px;height:410px;padding-top:40px;border:1px solid #ddd">
    <div class="script">Catering</div>
    <h3>Special Events</h3>
    <p style="text-align:left">Let our kitchen cater your next gathering with fresh seasonal dishes, warm service and a cozy room for family and friends.</p>
    <div class="btn btn-black" style="left:40px;top:300px;width:120px;height:38px;font-size:13px">More Details</div>
  </div>
  <div class="photo" role="img" aria-label="Banquet hall decorated in pink light" style="left:340px;top:2250px;width:260px;height:410px;background:radial-gradient(circle at 50% 40%,#f25aa0,#8c1c5c 60%,#3a0c28)"></div>
  <div class="ev-card" style="left:600px;top:2250px;width:260px;height:200px;padding-top:40px">
    <div class="script">Catering</div><h3>Social Events</h3><span class="more">More Detail</span>
  </div>
  <div class="photo" role="img" aria-label="Glasses raised in a toast" style="left:860px;top:2250px;width:260px;height:200px;background:linear-gradient(135deg,#c8b9a8,#6e5c4e 60%,#3c3330)"></div>
  <div class="photo" role="img" aria-label="Long dinner tables set for an event" style="left:600px;top:2450px;width:260px;height:210px;background:linear-gradient(160deg,#f0e6de,#c97a6e 50%,#6b3a36)"></div>
  <div class="ev-card" style="left:860px;top:2450px;width:260px;height:210px;padding-top:44px">
    <div class="script">Catering</div><h3>Corporate Events</h3><span class="more">More Detail</span>
  </div>
  <div class="btn btn-dark" style="left:520px;top:2700px;width:160px;height:42px">View All Event</div>
</section>

<section class="order">
  <div class="label" style="left:130px;top:90px">ORDER ONLINE</div>
  <div class="sub" style="left:130px;top:124px">www.brookmerecafe.com</div>
  <svg class="abs" style="left:420px;top:88px" width="40" height="40" viewBox="0 0 24 24"><path fill="none" stroke="#f6d80c" stroke-width="1.8" d="M3 9h18l-2 11H5zM8 9l4-6 4 6"/></svg>
  <svg class="abs" style="left:750px;top:88px" width="40" height="40" viewBox="0 0 24 24"><path fill="#f6d80c" d="M6.6 10.8a15 15 0 0 0 6.6 6.6l2.2-2.2a1 1 0 0 1 1-.25 11 11 0 0 0 3.6.6 1 1 0 0 1 1 1V20a1 1 0 0 1-1 1A17 17 0 0 1 3 4a1 1 0 0 1 1-1h3.5a1 1 0 0 1 1 1c0 1.25.2 2.45.6 3.6a1 1 0 0 1-.25 1z"/></svg>
  <div class="label" style="left:810px;top:90px">ORDER by PHONE</div>
  <div class="sub" style="left:810px;top:124px">(312) 555-0148</div>
</section>
<div class="order-plate" role="img" aria-label="Fresh salad served on a white plate"></div>

<section class="gallery">
  <div class="tabs"><span class="on">ALL</span><span>Lunch</span><span>Dinner</span><span>Burger</span><span>Desserts</span><span>Special Smoothies</span></div>
  <div class="photo" role="img" aria-label="Bowl of tomato stew" style="left:80px;top:3250px;width:340px;height:240px;background:radial-gradient(circle,#c1432a,#6a2418 55%,#3a2a22)"></div>
  <div class="photo" role="img" aria-label="Vegetable wraps on a plate" style="left:430px;top:3250px;width:340px;height:240px;background:radial-gradient(circle,#b7c35a,#7a8a3a 50%,#e9e2c6)"></div>
  <div class="photo" role="img" aria-label="Grilled sandwich halves" style="left:780px;top:3250px;width:340px;height:240px;background:radial-gradient(circle,#d9a04c,#a45e2a 55%,#f2ede4)"></div>
  <div class="photo" role="img" aria-label="Avocado toast" style="left:80px;top:3500px;width:250px;height:200px;background:radial-gradient(circle,#9cb84a,#5e7a2e 60%,#2f3a1c)"></div>
  <div class="photo" role="img" aria-label="Small bowls of dips" style="left:340px;top:3500px;width:260px;height:200px;background:radial-gradient(circle,#e3d6a2,#a6b46a 50%,#f4f1e8)"></div>
  <div class="photo" role="img" aria-label="Stacked club sandwich" style="left:610px;top:3500px;width:510px;height:400px;background:radial-gradient(circle at 55% 50%,#d6b27a,#9a6a3c 50%,#e9e4dc)"></div>
  <div class="photo" role="img" aria-label="Plate of sliced tomatoes" style="left:80px;top:3710px;width:250px;height:190px;background:radial-gradient(circle,#d0483a,#e8e4de 55%,#b8b2aa)"></div>
  <div class="photo" role="img" aria-label="Salad bowl with greens" style="left:340px;top:3710px;width:260px;height:190px;background:radial-gradient(circle,#8db04e,#4e6a2a 55%,#d9d4cc)"></div>
  <div class="btn btn-dark" style="left:540px;top:3930px;width:120px;height:42px">View All</div>
</section>

<footer class="footer">
  <h4 style="left:80px">Usefull Link</h4>
  <ul><li>Home</li><li>About Us</li><li>Menu</li><li>Location</li><li>Events</li><li>Photo Gallery</li><li>Online Order</li><li>Contact Us</li></ul>
  <h4 style="left:320px">Get In Touch</h4>
  <div class="row" style="top:96px">
    <svg width="20" height="22" viewBox="0 0 24 24"><path fill="#f6d80c" d="M12 2a7 7 0 0 0-7 7c0 5 7 13 7 13s7-8 7-13a7 7 0 0 0-7-7zm0 9.5A2.5 2.5 0 1 1 12 6.5a2.5 2.5 0 0 1 0 5z"/></svg>
    <div><b>Brookmere Cafe</b><br>4120 North Linden Avenue<br>Chicago, IL 60699</div>
  </div>
  <div class="row" style="top:190px">
    <svg width="20" height="20" viewBox="0 0 24 24"><path fill="#f6d80c" d="M6.6 10.8a15 15 0 0 0 6.6 6.6l2.2-2.2a1 1 0 0 1 1-.25 11 11 0 0 0 3.6.6 1 1 0 0 1 1 1V20a1 1 0 0 1-1 1A17 17 0 0 1 3 4a1 1 0 0 1 1-1h3.5a1 1 0 0 1 1 1c0 1.25.2 2.45.6 3.6a1 1 0 0 1-.25 1z"/></svg>
    <div>(312) 555-0148</div>
  </div>
  <div class="row" style="top:240px">
    <svg width="20" height="20" viewBox="0 0 24 24"><circle cx="12" cy="12" r="9" fill="none" stroke="#f6d80c" stroke-width="2"/><path d="M12 7v5l3 2" stroke="#f6d80c" stroke-width="2" fill="none"/></svg>
    <div><b>Mon – Fri</b> 8 am to 10 pm<br><b>Sat – Sun</b> 9 am to 11 pm</div>
  </div>
  <h4 style="left:600px">Location</h4>
  <div class="photo" role="img" aria-label="Street map of the cafe neighbourhood" style="left:600px;top:96px;width:220px;height:170px;background:linear-gradient(135deg,#e8eef2,#cfdbe4 50%,#bcd0c0)"></div>
  <div class="foot-brand"><span class="dot"></span><span class="name">Brookmere Cafe</span></div>
  <p class="abs" style="left:880px;top:150px;width:260px;color:#d8d2da;font-size:13px;line-height:1.6">Brookmere Cafe offers fresh dining and takeout for the whole neighborhood.</p>
</footer>
<div class="bottombar">© Brookmere Cafe 2017. All Rights Reserved.</div>

</body>
</html>
```